Creative - Appealing - Business Card Design Project

Looking for a Business card design (vector artwork) for an existing company called 'Fernway Sound'. We operate in the entertainment industry specializing in audio system design and rental, however; we also deal with other sectors of the entertainment industry including lighting, video, staging and power system design and rental. We would like to see designs that don't focus too much on audio but include elements encompassing everything else.

Double sided business card, following our new colour scheme and logo, which is attached. The card would ideally be creative and eye catching to draw in new customers in the elegant event production market, such as weddings & corporate affairs.

Target Market(s)

High end corporate clients, wedding clients

Industry/Entity Type

Entertainment

Requirements
Must have
• Our contact details, these can be worded & listed however you think appropriate as part as the design

Business Name - Fernway Sound
My Name - Dominic Harwell
Web Address - www.fernwaysound-example.com
Mobile Number - 07914 362 517
Office Number - 0330 481 7265
Email - dom@fernwaysound-example.com

The name, email and mobile number would need to be able to be changed to my business partners also.

The font used on our logo is Sansation
Nice to have
• On one side maybe a word cloud involving the services in which we can provide; Lighting, Sound, Event Production, Staging, LED Uplighting, Projection Mapping, Wedding Hire

On the other side, all the important credentials of contact.
Should not have
• The design should not use any old style fonts (i.e Times New Roman, Gothic etc) or on the other side of the scale, any 'jokey' fonts (i.e. Comic Sans).

The font to be used is Sansation

```html
<!DOCTYPE html>
<html lang="en">
<head>
<meta charset="utf-8">
<title>Fernway Sound – Business Card</title>
<link rel="stylesheet" href="https://fonts.googleapis.com/css2?family=Sansation:wght@400;700&display=swap">
<style>
  :root {
    --stage: #2b2b2d;
    --card-white: #f1f1f3;
    --card-grey: #d9d9e0;
    --purple: #5b3a9c;
    --purple-deep: #4a2d86;
    --purple-light: #7a5cb8;
    --text-grey: #7c7c82;
    --text-light: #d6d6de;
  }
  * { box-sizing: border-box; margin: 0; padding: 0; }
  html, body { width: 1200px; height: 900px; overflow: hidden; }
  body {
    background: var(--stage);
    font-family: "Sansation", "Trebuchet MS", sans-serif;
    position: relative;
  }
  .card {
    position: absolute;
    width: 560px;
    height: 320px;
    overflow: hidden;
    box-shadow: 0 18px 40px rgba(0,0,0,0.45);
  }
  .card svg.card-art { position: absolute; inset: 0; width: 100%; height: 100%; }

  /* Contact side */
  .card--contact { left: 90px; top: 100px; background: var(--card-white); }
  .contact-block { position: absolute; left: 290px; top: 70px; }
  .contact-name { color: var(--purple); font-size: 21px; font-weight: 400; margin-bottom: 10px; }
  .contact-list { list-style: none; color: var(--text-grey); font-size: 12.5px; line-height: 1.45; }
  .contact-list .label { display: inline-block; width: 16px; }
  .contact-web { margin-top: 14px; color: var(--text-grey); font-size: 12.5px; }
  .brand-block { position: absolute; left: 44px; top: 196px; display: flex; align-items: center; gap: 14px; }
  .brand-mark { width: 34px; height: 34px; background: var(--purple); }
  .brand-name {
    color: var(--text-grey); font-weight: 700; font-size: 34px;
    line-height: 0.95; text-transform: uppercase;
  }

  /* Services side */
  .card--services { left: 550px; top: 480px; background: var(--purple); }
  .services-brand { position: absolute; left: 60px; top: 92px; display: flex; align-items: center; gap: 16px; }
  .services-mark { width: 44px; height: 44px; border-radius: 50%; background: var(--text-light); }
  .services-name { color: var(--text-light); font-weight: 700; font-size: 40px; text-transform: uppercase; letter-spacing: 0.5px; }
  .services-web {
    position: absolute; left: 122px; top: 146px;
    color: var(--text-light); font-size: 12px; letter-spacing: 4px;
  }
  .services-list {
    position: absolute; left: 60px; top: 196px; width: 450px;
    color: var(--text-light); font-size: 15px; line-height: 1.35; text-align: center;
  }
  .services-list .sep { margin: 0 6px; opacity: 0.9; }
</style>
</head>
<body>

  <section class="card card--contact" aria-label="Contact side of business card">
    <svg class="card-art" viewBox="0 0 560 320" aria-hidden="true">
      <rect width="560" height="320" fill="var(--purple)"/>
      <polygon points="0,0 440,0 500,60 455,215 0,305" fill="var(--card-white)"/>
      <polygon points="440,0 560,0 560,40 500,60" fill="var(--purple-deep)"/>
      <polygon points="0,305 455,215 560,200 560,320 0,320" fill="var(--purple-light)" opacity="0.55"/>
      <polygon points="120,0 200,0 330,320 250,320" fill="var(--card-grey)" opacity="0.45"/>
      <polygon points="0,210 500,60 480,110 0,250" fill="var(--card-grey)" opacity="0.35"/>
    </svg>
    <div class="contact-block">
      <p class="contact-name">Dominic Harwell</p>
      <ul class="contact-list">
        <li><span class="label">M.</span>07914 362 517</li>
        <li><span class="label">O.</span>0330 481 7265</li>
        <li><span class="label">E.</span>dom@fernwaysound-example.com</li>
      </ul>
      <p class="contact-web">www.fernwaysound-example.com</p>
    </div>
    <div class="brand-block">
      <span class="brand-mark" aria-hidden="true"></span>
      <p class="brand-name">Fernway<br>Sound</p>
    </div>
  </section>

  <section class="card card--services" aria-label="Services side of business card">
    <svg class="card-art" viewBox="0 0 560 320" aria-hidden="true">
      <rect width="560" height="320" fill="var(--purple)"/>
      <polygon points="0,0 180,0 420,130 0,180" fill="var(--purple-light)" opacity="0.35"/>
      <polygon points="0,180 420,130 0,320" fill="var(--purple-deep)" opacity="0.35"/>
      <polygon points="60,0 120,0 260,320 190,320" fill="#ffffff" opacity="0.05"/>
    </svg>
    <div class="services-brand">
      <span class="services-mark" aria-hidden="true"></span>
      <p class="services-name">Fernway Sound</p>
    </div>
    <p class="services-web">www.fernwaysound-example.com</p>
    <p class="services-list">
      Lighting<span class="sep">|</span>Sound<span class="sep">|</span>Event Production<span class="sep">|</span>Staging<span class="sep">|</span>LED Uplighting<br>
      Projection Mapping<span class="sep">|</span>Wedding Hire
    </p>
  </section>

</body>
</html>
```